Home Inspection Flyer

Looking to have flyer designed that features our business, services, and our contact information. There are three of us. We are all business partners and do not have a company phone number. So each of us would need to be listed on flyer along with our individual phone number. Everything you could possibly need is on our website from logo to services and contact information. https://larkmeadowhomereview.com/. If you could possible incorporate our company colors that would be great. You can find those in our logo top left hand side of website and attached. Please also include our velcorant and brev logos ( home inspector affiliations ) on brochure as well. Those can be found on website. Please feel free to reach out with any questions.
Thanks
Dale
Updates
Looking to get a few tri fold designs. All the ones submitted have been 8x11

```html
<!DOCTYPE html>
<html lang="en">
<head>
<meta charset="utf-8">
<title>Larkmeadow Home Review – Home Inspection Flyer, Front and Back</title>
<link rel="stylesheet" href="https://fonts.googleapis.com/css2?family=Cinzel:wght@400;700&family=Roboto:wght@400;500;700&family=Roboto+Condensed:wght@500;700&display=swap">
<style>
  :root {
    --ink: #0d0d0d;
    --night: #1d1f20;
    --green: #6fe01c;
    --green-deep: #55b514;
    --paper: #ffffff;
    --text: #1a1a1a;
    --backdrop: #ececec;
  }
  * { box-sizing: border-box; margin: 0; padding: 0; }
  html, body { width: 773px; height: 1200px; overflow: hidden; background: var(--backdrop); }
  body { position: relative; font-family: "Roboto", Arial, sans-serif; color: var(--text); }
  ul { list-style: none; }

  /* Each page is built at 672 × 868 and scaled to fit the canvas */
  .page { position: absolute; left: 156px; width: 672px; height: 868px; background: var(--paper); overflow: hidden; transform: scale(0.684); transform-origin: 0 0; box-shadow: 0 2px 10px rgba(0,0,0,.18); }
  .page--front { top: 4px; }
  .page--back { top: 602px; }

  .hero-art { position: absolute; left: 0; top: 0; }

  .brand-box { position: absolute; background: #fff; display: flex; align-items: center; justify-content: center; gap: 7px; }
  .brand-mark { width: 10px; height: 10px; background: var(--ink); flex: none; }
  .brand-name { font-family: "Cinzel", serif; font-weight: 700; color: var(--ink); line-height: 1.15; }
  .page--front .brand-box { left: 33px; top: 9px; width: 124px; height: 86px; }
  .page--front .brand-name { font-size: 12px; }
  .page--back .brand-box { left: 463px; top: 25px; width: 178px; height: 112px; }
  .page--back .brand-name { font-size: 16px; }

  .headline { position: absolute; left: 30px; top: 100px; font-family: "Cinzel", serif; color: #fff; text-transform: uppercase; line-height: 1.04; }
  .headline .line { display: block; }
  .headline .l1 { font-size: 29px; }
  .headline .l2 { font-size: 42px; font-weight: 700; color: var(--green); letter-spacing: 1px; }
  .headline .l3 { font-size: 25px; }
  .headline .l4 { font-size: 31px; }
  .headline .l5 { font-size: 19px; margin-top: 2px; }

  .services-title { position: absolute; left: 25px; top: 344px; font-size: 19px; line-height: 1.2; color: var(--green-deep); font-weight: 500; text-transform: uppercase; }
  .services-title strong { color: var(--ink); font-weight: 700; }

  .service-row { position: absolute; left: 0; top: 408px; width: 672px; height: 70px; }
  .service { position: absolute; top: 0; width: 80px; }
  .service svg { width: 24px; height: 24px; display: block; }
  .service span { display: block; margin-top: 18px; font-size: 8px; font-weight: 700; line-height: 1.25; color: var(--ink); }

  .content { position: absolute; left: 25px; width: 612px; }
  .page--front .content { top: 488px; }
  .page--back .content { top: 325px; }
  .section-heading { font-weight: 700; font-size: 21px; color: var(--ink); }
  .tag { display: inline-block; background: var(--ink); color: var(--green); border: 2px solid var(--green); border-radius: 3px; font-family: "Roboto Condensed", sans-serif; font-weight: 500; font-size: 12.5px; line-height: 1.2; padding: 1px 5px; text-transform: uppercase; }
  .page--front .tag { margin-top: 20px; }
  .page--back .tag { margin-top: 24px; }
  .page--back .tag:first-child { margin-top: 0; }
  .content p { font-size: 8.2px; line-height: 1.32; color: var(--text); margin-top: 10px; }
  .tag + p { margin-top: 8px; }

  .contact-bar { position: absolute; left: 0; bottom: 0; width: 672px; height: 70px; background: var(--ink); display: flex; align-items: center; }
  .contact { width: 224px; display: flex; align-items: center; gap: 7px; padding-left: 24px; height: 50px; color: #fff; }
  .contact + .contact { border-left: 1px solid var(--green-deep); }
  .portrait { width: 44px; height: 44px; border-radius: 50%; background: radial-gradient(circle at 50% 40%, #c9a58a, #6c5446 70%, #2d2a28); border: 2px solid #fff; flex: none; }
  .contact-name { font-size: 9px; font-weight: 500; }
  .contact-line { display: flex; align-items: center; gap: 4px; font-size: 7.6px; margin-top: 2px; white-space: nowrap; }
  .contact-line svg { width: 7px; height: 7px; fill: var(--green); flex: none; }
</style>
</head>
<body>

<!-- Front page -->
<article class="page page--front">
  <svg class="hero-art" viewBox="0 0 672 362" width="672" height="362" xmlns="http://www.w3.org/2000/svg">
    <defs>
      <linearGradient id="frontBg" x1="0" y1="0" x2="1" y2="1">
        <stop offset="0" stop-color="#1d1f20"/>
        <stop offset="0.6" stop-color="#2a2c2d"/>
        <stop offset="1" stop-color="#111213"/>
      </linearGradient>
      <linearGradient id="coupleTone" x1="0" y1="0" x2="1" y2="1">
        <stop offset="0" stop-color="#d9d4cc"/>
        <stop offset="0.45" stop-color="#8a6a55"/>
        <stop offset="0.8" stop-color="#8fa7c4"/>
        <stop offset="1" stop-color="#5f7fa6"/>
      </linearGradient>
    </defs>
    <g role="img" aria-label="Dark, faded photo of a house exterior behind the headline">
      <path d="M0 0 H672 V258 H385 Q190 262 0 306 Z" fill="url(#frontBg)"/>
    </g>
    <path d="M0 316 Q190 272 385 262 L385 274 Q190 292 0 348 Z" fill="var(--green)"/>
    <g role="img" aria-label="Photo of a smiling couple embracing, framed in a house outline">
      <path d="M385 358 V200 H352 L538 8 L642 110 V40 H668 V136 L670 138 V358 Z" fill="url(#coupleTone)" stroke="var(--green)" stroke-width="4" stroke-linejoin="round"/>
    </g>
  </svg>

  <div class="brand-box">
    <span class="brand-mark"></span>
    <span class="brand-name">Larkmeadow<br>Home Review</span>
  </div>

  <h1 class="headline">
    <span class="line l1">A Home Buyer</span>
    <span class="line l2">Inspection</span>
    <span class="line l3">Is the Smart Move</span>
    <span class="line l4">But Don't Take</span>
    <span class="line l5">Our Word for It</span>
  </h1>

  <h2 class="services-title">Larkmeadow Home Review<br>Inspection <strong>Services</strong></h2>

  <ul class="service-row">
    <li class="service" style="left:25px">
      <svg viewBox="0 0 24 24"><path d="M12 3 L2 12 H5 V21 H10 V15 H14 V21 H19 V12 H22 Z" fill="var(--ink)"/></svg>
      <span>Home<br>Inspection</span>
    </li>
    <li class="service" style="left:114px">
      <svg viewBox="0 0 24 24" fill="none" stroke="var(--ink)" stroke-width="2"><ellipse cx="12" cy="14" rx="5" ry="7" fill="var(--ink)"/><path d="M7 10 L2 7 M7 14 H2 M7 18 L2 21 M17 10 L22 7 M17 14 H22 M17 18 L22 21 M10 6 L8 2 M14 6 L16 2"/></svg>
      <span>Pest<br>Inspection</span>
    </li>
    <li class="service" style="left:195px">
      <svg viewBox="0 0 24 24" fill="none" stroke="var(--ink)" stroke-width="2"><path d="M10 3 H14 V14 A4 4 0 1 1 10 14 Z"/><circle cx="12" cy="17" r="2" fill="var(--ink)"/></svg>
      <span>Radon<br>Inspection</span>
    </li>
    <li class="service" style="left:287px">
      <svg viewBox="0 0 24 24" fill="none" stroke="var(--ink)" stroke-width="2"><path d="M5 2 H15 L19 6 V22 H5 Z"/><rect x="8" y="11" width="6" height="6" fill="var(--ink)"/><path d="M14 13 L17 11 V17 L14 15"/></svg>
      <span>Sewer Camera<br>Inspection</span>
    </li>
    <li class="service" style="left:393px">
      <svg viewBox="0 0 24 24" fill="var(--ink)"><path d="M3 4 H7 V8 H15 A4 4 0 0 1 19 12 V14 H15 V12 H7 V16 H3 Z"/><circle cx="17" cy="18" r="1.5"/><circle cx="20" cy="21" r="1.2"/></svg>
      <span>Water Sample<br>Test</span>
    </li>
    <li class="service" style="left:479px">
      <svg viewBox="0 0 24 24" fill="var(--ink)"><circle cx="4" cy="6" r="2"/><circle cx="10" cy="6" r="2"/><circle cx="16" cy="6" r="2"/><circle cx="4" cy="12" r="2"/><circle cx="10" cy="12" r="2"/><circle cx="20" cy="12" r="2"/><circle cx="4" cy="18" r="2"/><circle cx="16" cy="18" r="2"/><circle cx="20" cy="18" r="2"/></svg>
      <span>Well Flow<br>Test</span>
    </li>
    <li class="service" style="left:579px">
      <svg viewBox="0 0 24 24" fill="none" stroke="var(--ink)" stroke-width="2.4"><path d="M2 7 Q7 3 12 7 T22 7 M2 13 Q7 9 12 13 T22 13 M2 19 Q7 15 12 19 T22 19"/></svg>
      <span>Septic Dye<br>Flow Test</span>
    </li>
  </ul>

  <section class="content">
    <h2 class="section-heading">HOME INSPECTION SERVICES</h2>

    <h3 class="tag">Best Home Inspection Service</h3>
    <p>Our Home Inspection is a personal, non-invasive examination of the structural and living areas of a home's current state. This type of checkup is often associated with the sale or purchase of the real estate. Our professionally trained and certified Home Inspectors will direct the inspection, and prepare and submit a full examination report, so you can be confident about the condition of the property.</p>
    <p>Our report covers all critical components of the home but does not warranty the effectiveness of the home's systems or protect it from future issues that may arise following the inspection. Instead, our Home Inspection provides buyers, sellers, and lenders important insight into the property's conditions before the sale or purchase.</p>
    <p>We know that finding the right home can be risky especially when you compare the price with the condition. The best way to safeguard your deal is a Home Inspection before you sign on the line.</p>

    <h3 class="tag">Home Inspection for All Kinds of Buyers</h3>
    <p>Homes in Southwest PA are unique and require a keen home inspector that has an eye for detail. It's smart to trust a reputable company like LHR that is locally owned and operated.</p>
    <p>At Larkmeadow Home Review, our customers are encouraged to participate and walk alongside our home professional and ask questions to get first-hand information and instant feedback regarding possible repairs and maintenance tips. Our no-pressure checkup is thorough and educational.</p>
  </section>

  <footer class="contact-bar">
    <div class="contact">
      <div class="portrait" role="img" aria-label="Portrait photo of Corwin Vale"></div>
      <div>
        <div class="contact-name">Corwin Vale</div>
        <div class="contact-line"><svg viewBox="0 0 24 24"><path d="M6.6 10.8a15 15 0 0 0 6.6 6.6l2.2-2.2a1 1 0 0 1 1-.25 11.4 11.4 0 0 0 3.6.57 1 1 0 0 1 1 1V20a1 1 0 0 1-1 1A17 17 0 0 1 3 4a1 1 0 0 1 1-1h3.5a1 1 0 0 1 1 1 11.4 11.4 0 0 0 .57 3.6 1 1 0 0 1-.25 1Z"/></svg>(555) 014-3271</div>
        <div class="contact-line"><svg viewBox="0 0 24 24"><path d="M2 5h20v14H2Z"/></svg>corwin@larkmeadow.example</div>
      </div>
    </div>
    <div class="contact">
      <div class="portrait" role="img" aria-label="Portrait photo of Tobin Marsh"></div>
      <div>
        <div class="contact-name">Tobin Marsh</div>
        <div class="contact-line"><svg viewBox="0 0 24 24"><path d="M6.6 10.8a15 15 0 0 0 6.6 6.6l2.2-2.2a1 1 0 0 1 1-.25 11.4 11.4 0 0 0 3.6.57 1 1 0 0 1 1 1V20a1 1 0 0 1-1 1A17 17 0 0 1 3 4a1 1 0 0 1 1-1h3.5a1 1 0 0 1 1 1 11.4 11.4 0 0 0 .57 3.6 1 1 0 0 1-.25 1Z"/></svg>(555) 019-0201</div>
        <div class="contact-line"><svg viewBox="0 0 24 24"><path d="M2 5h20v14H2Z"/></svg>tobin@larkmeadow.example</div>
      </div>
    </div>
    <div class="contact">
      <div class="portrait" role="img" aria-label="Portrait photo of Dale Fenrow"></div>
      <div>
        <div class="contact-name">Dale Fenrow</div>
        <div class="contact-line"><svg viewBox="0 0 24 24"><path d="M6.6 10.8a15 15 0 0 0 6.6 6.6l2.2-2.2a1 1 0 0 1 1-.25 11.4 11.4 0 0 0 3.6.57 1 1 0 0 1 1 1V20a1 1 0 0 1-1 1A17 17 0 0 1 3 4a1 1 0 0 1 1-1h3.5a1 1 0 0 1 1 1 11.4 11.4 0 0 0 .57 3.6 1 1 0 0 1-.25 1Z"/></svg>(555) 027-0073</div>
        <div class="contact-line"><svg viewBox="0 0 24 24"><path d="M2 5h20v14H2Z"/></svg>dale@larkmeadow.example</div>
      </div>
    </div>
  </footer>
</article>

<!-- Back page -->
<article class="page page--back">
  <svg class="hero-art" viewBox="0 0 672 310" width="672" height="310" xmlns="http://www.w3.org/2000/svg">
    <defs>
      <linearGradient id="houseTone" x1="0" y1="0" x2="1" y2="1">
        <stop offset="0" stop-color="#c9d2dc"/>
        <stop offset="0.5" stop-color="#9aa1a8"/>
        <stop offset="0.8" stop-color="#6b6660"/>
        <stop offset="1" stop-color="#c98d4e"/>
      </linearGradient>
      <linearGradient id="familyTone" x1="0" y1="0" x2="1" y2="1">
        <stop offset="0" stop-color="#eeeae4"/>
        <stop offset="0.5" stop-color="#d7c2ad"/>
        <stop offset="1" stop-color="#8ea8c6"/>
      </linearGradient>
    </defs>
    <g role="img" aria-label="Photo of a modern two-storey house under a cloudy sky">
      <path d="M0 0 H672 V238 Q380 232 0 288 Z" fill="url(#houseTone)"/>
    </g>
    <path d="M0 252 Q170 240 330 266 L330 272 Q160 262 0 300 Z" fill="var(--ink)"/>
    <path d="M0 272 Q200 248 672 236 L672 242 Q220 262 0 300 Z" fill="var(--green)"/>
    <g role="img" aria-label="Photo of a young family with a baby sitting under a house shape">
      <path d="M72 292 V146 H46 L203 16 L258 62 V40 H290 V92 L318 118 H296 V292 Z" fill="url(#familyTone)" stroke="var(--green)" stroke-width="4" stroke-linejoin="round"/>
    </g>
  </svg>

  <div class="brand-box">
    <span class="brand-mark"></span>
    <span class="brand-name">Larkmeadow<br>Home Review</span>
  </div>

  <section class="content">
    <h3 class="tag">Home Analysis for All Size Properties</h3>
    <p>LHR offers comprehensive inspection and testing services for all types of properties, but we concentrate on residential inspections and testing services in Southwest Pennsylvania.</p>
    <p>Our examination will cover virtually every critical dwelling component. If something isn't correct or not up to code it will be noted in our digital home inspection report.</p>
    <p>Did you know that Pittsburgh's real estate market is one of the best investment markets? But do your homework and get a home inspection before you buy to maximize your ROI.</p>

    <h3 class="tag">LHR Is Your House &amp; Home Inspection Experts</h3>
    <p>Our home inspectors are experts in the field. We'll produce a simple and easy-to-understand report full of professional advice. It will also contain solutions and/or alternatives to what we find that might be cause for concern.</p>
    <p>Our time spent together will be transparent and truthful. You may ask our home inspector questions along the way, and we'll provide instant feedback regarding concerns about repairs, safety, and maintenance.</p>

    <h3 class="tag">Home Inspection to Protect Your Family &amp; Investment</h3>
    <p>LHR cares about your family and understands the weight of your investment. We use our experience, training, and education to examine the property from top to bottom to compile a comprehensive home inspection report.</p>
    <p>Some homeowners consider our examination a home health inspection because we look for safety regulations, code violations, and structural encroachments.</p>
    <p>Our HI's are your best ally and we encourage our customers to ask questions. Nothing is off the table. We will take the time to address your questions and concerns. This one-on-one time is your chance to learn how to protect your investment.</p>

    <h3 class="tag">Larkmeadow Home Review Is Your Hometown Choice</h3>
    <p>We understand that the examination process can feel a bit intrusive and our report may cover sensitive or private issues in and outside the home.</p>
    <p>Therefore, to protect your privacy, we don't share your report or confidential information.</p>
  </section>

  <footer class="contact-bar">
    <div class="contact">
      <div class="portrait" role="img" aria-label="Portrait photo of Corwin Vale"></div>
      <div>
        <div class="contact-name">Corwin Vale</div>
        <div class="contact-line"><svg viewBox="0 0 24 24"><path d="M6.6 10.8a15 15 0 0 0 6.6 6.6l2.2-2.2a1 1 0 0 1 1-.25 11.4 11.4 0 0 0 3.6.57 1 1 0 0 1 1 1V20a1 1 0 0 1-1 1A17 17 0 0 1 3 4a1 1 0 0 1 1-1h3.5a1 1 0 0 1 1 1 11.4 11.4 0 0 0 .57 3.6 1 1 0 0 1-.25 1Z"/></svg>(555) 014-3271</div>
        <div class="contact-line"><svg viewBox="0 0 24 24"><path d="M2 5h20v14H2Z"/></svg>corwin@larkmeadow.example</div>
      </div>
    </div>
    <div class="contact">
      <div class="portrait" role="img" aria-label="Portrait photo of Tobin Marsh"></div>
      <div>
        <div class="contact-name">Tobin Marsh</div>
        <div class="contact-line"><svg viewBox="0 0 24 24"><path d="M6.6 10.8a15 15 0 0 0 6.6 6.6l2.2-2.2a1 1 0 0 1 1-.25 11.4 11.4 0 0 0 3.6.57 1 1 0 0 1 1 1V20a1 1 0 0 1-1 1A17 17 0 0 1 3 4a1 1 0 0 1 1-1h3.5a1 1 0 0 1 1 1 11.4 11.4 0 0 0 .57 3.6 1 1 0 0 1-.25 1Z"/></svg>(555) 019-0201</div>
        <div class="contact-line"><svg viewBox="0 0 24 24"><path d="M2 5h20v14H2Z"/></svg>tobin@larkmeadow.example</div>
      </div>
    </div>
    <div class="contact">
      <div class="portrait" role="img" aria-label="Portrait photo of Dale Fenrow"></div>
      <div>
        <div class="contact-name">Dale Fenrow</div>
        <div class="contact-line"><svg viewBox="0 0 24 24"><path d="M6.6 10.8a15 15 0 0 0 6.6 6.6l2.2-2.2a1 1 0 0 1 1-.25 11.4 11.4 0 0 0 3.6.57 1 1 0 0 1 1 1V20a1 1 0 0 1-1 1A17 17 0 0 1 3 4a1 1 0 0 1 1-1h3.5a1 1 0 0 1 1 1 11.4 11.4 0 0 0 .57 3.6 1 1 0 0 1-.25 1Z"/></svg>(555) 027-0073</div>
        <div class="contact-line"><svg viewBox="0 0 24 24"><path d="M2 5h20v14H2Z"/></svg>dale@larkmeadow.example</div>
      </div>
    </div>
  </footer>
</article>

</body>
</html>
```